International Petrochemical business needs a web design for Tessaro Desk system

We need a web design for a "Tessaro Desk" system for an international petrochemical company. The web site is used internally within the company. It is hosted by an internal department which provides government permit request service for other departments.

We would like to see designs of two pages using color light blue. (home page, internal page as attached).
Home Page:
1. Header has a background image and small animation. Header on home page can be taller than the header of the internal page.
2. Layout as attached.

Internal Page:
1. Header can use the same background image as the home page and can be shorter to utilize the page for content.
2. The blue icon behind every captions represent an icon. When user move mouse over this icon, it displays the caption in Thai language as a tooltip. This icon needs to be redesign.

The final design should communicate the followings:
- Excellent service provided system in terms of time and accurary
- Rapid growth of business via building petrochemical refinery plant

For Internal Page, the blue circle behind every captions represent an icon. When mouse over this icon, a tool tip showing the caption in Thai language is shown. Please also design this icon..

There are more feedbacks from customer as followed:

1. Banner should consists of 
    1.1 "Approved" stamp on paper
    1.2 An image of Garuda. It is used on every government documents in Thailand
    1.3 Image of petrochemical plant
2. Each menu item (Home, Permit, Search, etc) should have different colors. Drop down menu will use the same color as its parent menu item.
3. Overall tone of the web page should be light blue with background of the body the web page in white
4. "New Request" button should use green color with icon on it
5. Table header of each box in the body of the page should use dark blue background with text in white

Please kindly submit your revisions.
Thank you.

Reason: We get some late feedbacks from customers which was just updated to all designers.

• 1. Design for 1024x768 screen resolution
2. Use light blue theme
3. Background of header where the company logo is must have white background

```html
<!DOCTYPE html>
<html lang="en">
<head>
<meta charset="utf-8">
<title>Tessaro Desk</title>
<link href="https://fonts.googleapis.com/css2?family=Ubuntu:wght@400;500;700&family=Roboto:wght@400;500&family=Sarabun:wght@400&display=swap" rel="stylesheet">
<style>
:root{
  --ink:#222;
  --sky:#1a9be0;
  --sky-title:#2a9fe0;
  --head-top:#17c1f0;
  --head-bottom:#0a8fcc;
  --row-alt:#eef7fd;
  --link:#1a7fd0;
  --navy:#1b5a9e;
  --tab-home:#5fcdef;
  --tab-permits:#1fc79f;
  --tab-search:#f4b41a;
  --tab-report:#e6333d;
  --tab-admin:#56c13a;
  --tab-help:#a140cf;
  --drop:#1f9dbe;
  --green-top:#4fc24a;
  --green-bottom:#1e8f25;
  --pager-line:#d4d4d4;
  --pager-text:#999;
}
*{box-sizing:border-box;margin:0;padding:0}
html,body{width:1109px;height:1200px;overflow:hidden;background:#fff}
body{font-family:"Roboto",sans-serif;color:var(--ink)}
.page{position:relative;width:1000px;height:1082px;transform:scale(1.109);transform-origin:0 0}
.abs{position:absolute}
.topline{left:0;top:0;width:1000px;height:4px;background:var(--navy)}
.brand{left:45px;top:22px;display:flex;align-items:center;gap:8px}
.brand-dot{width:34px;height:34px;border-radius:50%;background:var(--sky)}
.brand-name{font-family:"Ubuntu",sans-serif;font-weight:700;font-size:19px;color:var(--navy);line-height:1}
.app-title{right:38px;top:32px;font-family:"Ubuntu",sans-serif;font-weight:700;font-size:35px;color:var(--sky);letter-spacing:.5px}
.nav{left:32px;top:82px;display:flex;gap:13px}
.tab{width:88px;height:30px;border-radius:6px 6px 0 0;color:#fff;font-family:"Ubuntu",sans-serif;font-size:14px;text-transform:uppercase;display:flex;align-items:center;justify-content:center;box-shadow:inset 0 8px 10px rgba(255,255,255,.25)}
.tab-home{background:var(--tab-home)}
.tab-permits{background:var(--tab-permits)}
.tab-search{background:var(--tab-search)}
.tab-report{background:var(--tab-report)}
.tab-admin{background:var(--tab-admin)}
.tab-help{background:var(--tab-help)}
.banner{left:0;top:112px;width:1000px;height:131px;background:linear-gradient(90deg,#0d1e44 0%,#1c3560 30%,#5a4a3a 50%,#1d3a6c 75%,#2a4574 100%)}
.stamp{left:760px;top:122px;width:190px;height:106px;border-radius:10px;background:linear-gradient(135deg,#c9cfd8,#8d97a8);opacity:.55}
.dropdown{left:32px;top:112px;width:134px;background:var(--drop)}
.dropdown a{display:block;height:26px;line-height:26px;padding-left:11px;font-family:"Ubuntu",sans-serif;font-size:11.5px;color:#fff;text-decoration:none;border-bottom:1px solid rgba(255,255,255,.6)}
.dropdown a:last-child{border-bottom:none}
.section-title{font-family:"Ubuntu",sans-serif;font-weight:500;font-size:17px;color:var(--sky-title);letter-spacing:.3px}
.panel{background:#fff;border-radius:4px;box-shadow:0 0 5px rgba(0,0,0,.25);overflow:hidden}
.panel table{width:100%;border-collapse:collapse;font-size:14px}
.panel th{height:44px;text-align:left;font-family:"Ubuntu",sans-serif;font-weight:400;font-size:14px;color:#fff;background:linear-gradient(var(--head-top),var(--head-bottom));padding-left:12px}
.panel td{height:24px;padding-left:12px}
.panel tbody tr:first-child td{padding-top:6px;height:30px}
.panel tbody tr:nth-child(even){background:var(--row-alt)}
.panel a{color:var(--link)}
.thai{font-family:"Sarabun",sans-serif;font-size:14px}
.due{display:inline-flex;align-items:center;gap:30px}
.pager{display:flex;gap:6px;font-size:14px;color:var(--link)}
.pager span{display:flex;align-items:center;justify-content:center;height:22px;border:1px solid var(--pager-line);background:#fff}
.pager .edge{width:44px;color:var(--pager-text);background:#f3f3f3}
.pager .nums{display:flex;border:none;background:none}
.pager .nums span{width:26px;margin-left:-1px}
.pager .nums span:first-child{color:var(--pager-text);background:#f3f3f3;margin-left:0}
.new-request{left:627px;top:766px;width:340px;height:54px;border-radius:10px;background:linear-gradient(var(--green-top),var(--green-bottom));border:1px solid #1a7a1f;display:flex;align-items:center;justify-content:center;gap:14px;color:#fff;font-family:"Ubuntu",sans-serif;font-weight:700;font-size:21px;letter-spacing:.5px}
.footer{left:0;top:1037px;width:1000px;height:45px;background:var(--navy);color:#fff;font-size:9.5px;display:flex;align-items:center;justify-content:space-between;padding:0 48px}
</style>
</head>
<body>
<div class="page">
  <div class="abs topline"></div>
  <div class="abs brand"><span class="brand-dot"></span><span class="brand-name">Veltrane Chemical</span></div>
  <div class="abs app-title">TESSARO DESK</div>

  <nav class="abs nav">
    <div class="tab tab-home">Home</div>
    <div class="tab tab-permits">Permits</div>
    <div class="tab tab-search">Search</div>
    <div class="tab tab-report">Report</div>
    <div class="tab tab-admin">Admin</div>
    <div class="tab tab-help">Help</div>
  </nav>

  <div class="abs banner" role="img" aria-label="Night view of an illuminated petrochemical refinery with a national emblem and an approved stamp on paper"></div>
  <div class="abs stamp" role="img" aria-label="Approved stamp on paper"></div>
  <div class="abs dropdown">
    <a>Create New Permit</a>
    <a>Transfer Role</a>
    <a>Transfer Res. Person</a>
  </div>

  <h2 class="abs section-title" style="left:42px;top:254px">New Requests</h2>
  <div class="abs panel" style="left:31px;top:281px;width:398px;height:181px">
    <table>
      <thead><tr><th style="width:118px">Request No.</th><th style="width:178px">Requested Date</th><th>Branch</th></tr></thead>
      <tbody>
        <tr><td>20013 - 0001</td><td>20/4/2013</td><td>GC1</td></tr>
        <tr><td>20013 - 0002</td><td>21/4/2013</td><td>GC2</td></tr>
        <tr><td>20013 - 0003</td><td>22/4/2013</td><td>GC3</td></tr>
        <tr><td>20013 - 0004</td><td>23/4/2013</td><td>GC4</td></tr>
        <tr><td>20013 - 0005</td><td>24/4/2013</td><td>GC5</td></tr>
      </tbody>
    </table>
  </div>
  <div class="abs pager" style="right:571px;top:477px"><span class="edge">PREV</span><span class="nums"><span>1</span><span>2</span><span>3</span><span>4</span><span>5</span></span><span class="edge">NEXT</span></div>

  <h2 class="abs section-title" style="left:460px;top:253px">My Working Requests</h2>
  <div class="abs panel" style="left:449px;top:281px;width:517px;height:181px">
    <table>
      <thead><tr><th style="width:115px">Request No.</th><th style="width:178px">Requested Date</th><th>Status</th></tr></thead>
      <tbody>
        <tr><td><a>56-0003</a></td><td>20/4/2013</td><td>Waiting for process</td></tr>
        <tr><td><a>56-0004</a></td><td>21/4/2013</td><td>In progress</td></tr>
        <tr><td><a>56-0005</a></td><td>20/4/2013</td><td>Incomplete document</td></tr>
        <tr><td><a>56-0006</a></td><td>21/4/2013</td><td>Cancel requested</td></tr>
        <tr><td><a>56-0007</a></td><td>22/4/2013</td><td>Cancel requested</td></tr>
      </tbody>
    </table>
  </div>
  <div class="abs pager" style="right:34px;top:477px"><span class="edge">PREV</span><span class="nums"><span>1</span><span>2</span><span>3</span><span>4</span><span>5</span></span><span class="edge">NEXT</span></div>

  <h2 class="abs section-title" style="left:41px;top:513px">Expiring Permits</h2>
  <div class="abs panel" style="left:31px;top:538px;width:935px;height:177px">
    <table>
      <thead><tr><th style="width:116px">Document No</th><th style="width:120px">Expire Date</th><th style="width:178px">Document Name</th><th style="width:117px">Branch</th><th style="width:188px">Processing Time (day)</th><th>Due Date</th></tr></thead>
      <tbody>
        <tr><td><a>AB56001</a></td><td>25/3/2013</td><td>Permit Name ###10</td><td>GC1</td><td>30</td><td><span class="due">-40 <svg width="14" height="14"><circle cx="7" cy="7" r="6" fill="#e12a2a"/></svg></span></td></tr>
        <tr><td><a>BIO5502</a></td><td>24/3/2013</td><td>Permit Name ###20</td><td>GC2</td><td>60</td><td><span class="due">-15 <svg width="14" height="14"><circle cx="7" cy="7" r="6" fill="#f5c20f"/></svg></span></td></tr>
        <tr><td><a>AB56001</a></td><td>23/3/2013</td><td>Permit Name ###10</td><td>GC3</td><td>30</td><td><span class="due">-40 <svg width="14" height="14"><circle cx="7" cy="7" r="6" fill="#e12a2a"/></svg></span></td></tr>
        <tr><td><a>BIO5502</a></td><td>22/3/2013</td><td>Permit Name ###12</td><td>GC4</td><td>60</td><td><span class="due">-15 <svg width="14" height="14"><circle cx="7" cy="7" r="6" fill="#f5c20f"/></svg></span></td></tr>
        <tr><td><a>BIO5502</a></td><td>21/3/2013</td><td>Permit Name ###13</td><td>GC5</td><td>30</td><td><span class="due">-40 <svg width="14" height="14"><circle cx="7" cy="7" r="6" fill="#f5c20f"/></svg></span></td></tr>
      </tbody>
    </table>
  </div>
  <div class="abs pager" style="right:34px;top:725px"><span class="edge">PREV</span><span class="nums"><span>1</span><span>2</span><span>3</span><span>4</span><span>5</span></span><span class="edge">NEXT</span></div>

  <h2 class="abs section-title" style="left:44px;top:779px">My In Progress Requests</h2>
  <div class="abs panel" style="left:30px;top:805px;width:578px;height:184px">
    <table>
      <thead><tr><th style="width:114px">Request No</th><th style="width:180px">Requested Date</th><th>Status</th></tr></thead>
      <tbody>
        <tr><td><a>56-0001</a></td><td>20/4/2013</td><td class="thai">ระหว่างดำเนินการ</td></tr>
        <tr><td><a>56-0002</a></td><td>21/4/2013</td><td class="thai">รอดำเนินการ</td></tr>
        <tr><td><a>56-0001</a></td><td>20/4/2013</td><td class="thai">ระหว่างดำเนินการ</td></tr>
        <tr><td><a>56-0002</a></td><td>19/4/2013</td><td class="thai">รอดำเนินการ</td></tr>
        <tr><td><a>56-0001</a></td><td>18/4/2013</td><td class="thai">ระหว่างดำเนินการ</td></tr>
      </tbody>
    </table>
  </div>
  <div class="abs pager" style="right:392px;top:998px"><span class="edge">PREV</span><span class="nums"><span>1</span><span>2</span><span>3</span><span>4</span><span>5</span></span><span class="edge">NEXT</span></div>

  <div class="abs new-request">
    <svg width="34" height="34" viewBox="0 0 34 34" aria-hidden="true">
      <rect x="2" y="5" width="24" height="26" fill="none" stroke="#fff" stroke-width="3"/>
      <path d="M14 22 L29 5 L33 9 L18 26 L13 27 Z" fill="#fff"/>
    </svg>
    NEW REQUEST
  </div>

  <h2 class="abs section-title" style="left:632px;top:832px">Recent Completed Requests</h2>
  <div class="abs panel" style="left:627px;top:860px;width:339px;height:129px">
    <table>
      <thead><tr><th style="width:178px">Request No.</th><th>Completed Date</th></tr></thead>
      <tbody>
        <tr><td><a>55-0100</a></td><td>25/3/2013</td></tr>
        <tr><td><a>55-0088</a></td><td>24/3/2013</td></tr>
        <tr><td><a>55-0002</a></td><td>18/1/2013</td></tr>
      </tbody>
    </table>
  </div>
  <div class="abs pager" style="right:34px;top:998px"><span class="edge">PREV</span><span class="nums"><span>1</span><span>2</span><span>3</span><span>4</span><span>5</span></span><span class="edge">NEXT</span></div>

  <footer class="abs footer">
    <span>Copyright © 2013 VeltraneChemical. All rights reserved.</span>
    <span>Terms and Condition | Privacy</span>
  </footer>
</div>
</body>
</html>
```